Orbell Consulting- executive coaching business

looking for business card design for a newly started coaching business.
specialising in Exective coaching, Leadership, NLP and Motivation.
Looking for a simple, classy design using the existing logo attached and colour themes that complement the logo.
No red or orange in the business card design please.

Target Market(s)

Defence and Veteran community

Industry/Entity Type

Life Coaching

Contact Information for Business Card

looking for business cards for newly started coaching business.
specialising in Exective Coaching, Leadership, NLP and Motivation

Font styles to use
Serif
Script

Colors
0556a4
3176b5
86cfc6
33b8a4

Requirements
Must have
• Logo
• Email address- Jess@orbellconsulting.com.au
• Contact number
• Services provided - Executive Coaching, Leadership, NLP and Motivational Mapping.
Nice to have
• Same colours as logo
Should not have
• Red or orange

```html
<!DOCTYPE html>
<html lang="en">
<head>
<meta charset="utf-8">
<title>Orbell Consulting – Business Cards</title>
<link href="https://fonts.googleapis.com/css2?family=Montserrat:wght@600&family=Open+Sans:ital,wght@0,400;0,600;0,700;1,600&display=swap" rel="stylesheet">
<style>
  :root {
    --backdrop: #eceef1;
    --card-white: #ffffff;
    --brand-blue: #1174bb;
    --brand-green: #2bb673;
    --mark-grey: #9a9a9a;
    --text-white: #ffffff;
  }
  * { margin: 0; padding: 0; box-sizing: border-box; }
  html, body {
    width: 1200px; height: 900px; overflow: hidden;
    background: var(--backdrop);
    font-family: "Open Sans", Arial, sans-serif;
  }
  .canvas { position: relative; width: 1200px; height: 900px; }
  .card {
    position: absolute;
    background: var(--card-white);
    box-shadow: 0 6px 18px rgba(0,0,0,0.15);
    overflow: hidden;
  }
  .card--front { left: 78px; top: 34px; width: 588px; height: 364px; }
  .card--back { left: 388px; top: 505px; width: 567px; height: 352px; }
  .card__bands { position: absolute; inset: 0; }
  .brand {
    position: absolute;
    display: flex; align-items: center; gap: 18px;
  }
  .card--front .brand { left: 72px; top: 53px; }
  .card--back .brand { left: 62px; top: 50px; }
  .brand__dot {
    width: 96px; height: 96px; border-radius: 50%;
    border: 3px solid var(--mark-grey);
    flex: none;
  }
  .brand__name {
    font-family: "Montserrat", Arial, sans-serif;
    font-weight: 600; font-size: 29px; letter-spacing: 0.2px;
    color: var(--brand-blue);
    white-space: nowrap;
    margin-bottom: 24px;
  }
  .card__panel {
    position: absolute; left: 0; right: 0;
    text-align: center; color: var(--text-white);
  }
  .card--front .card__panel { top: 234px; }
  .card--back .card__panel { top: 232px; }
  .person__name { font-size: 22px; font-weight: 700; line-height: 1.2; }
  .person__role { font-size: 15px; font-weight: 400; }
  .contact {
    display: flex; justify-content: center; gap: 36px;
    margin-top: 30px; font-size: 17px;
  }
  .contact__item { display: flex; align-items: center; gap: 5px; }
  .contact__item svg { fill: var(--text-white); }
  .services__title { font-size: 21px; font-weight: 700; margin-top: 28px; letter-spacing: 0.3px; }
  .services__list { font-size: 15.5px; font-weight: 600; font-style: italic; margin-top: 10px; }
</style>
</head>
<body>
<main class="canvas">

  <section class="card card--front">
    <svg class="card__bands" width="588" height="364" viewBox="0 0 588 364">
      <polygon points="0,188 402,188 380,214 0,214" fill="var(--brand-green)"/>
      <polygon points="0,218 386,218 416,180 588,180 588,364 0,364" fill="var(--brand-blue)"/>
    </svg>
    <div class="brand">
      <span class="brand__dot"></span>
      <span class="brand__name">ORBELL CONSULTING</span>
    </div>
    <div class="card__panel">
      <p class="person__name">Daniel Hartley</p>
      <p class="person__role">Managing Director</p>
      <div class="contact">
        <span class="contact__item">
          <svg width="12" height="12" viewBox="0 0 24 24"><path d="M6.6 10.8a15.1 15.1 0 0 0 6.6 6.6l2.2-2.2a1 1 0 0 1 1-.25 11.4 11.4 0 0 0 3.6.57 1 1 0 0 1 1 1V20a1 1 0 0 1-1 1A17 17 0 0 1 3 4a1 1 0 0 1 1-1h3.5a1 1 0 0 1 1 1c0 1.25.2 2.45.57 3.57a1 1 0 0 1-.25 1z"/></svg>
          (044)-555-0182
        </span>
        <span class="contact__item">
          <svg width="13" height="10" viewBox="0 0 26 20"><path d="M0 0h26v20H0z M2 3v1l11 7 11-7V3L13 10z" fill-rule="evenodd"/></svg>
          info@orbellcoaching.example
        </span>
      </div>
    </div>
  </section>

  <section class="card card--back">
    <svg class="card__bands" width="567" height="352" viewBox="0 0 567 352">
      <polygon points="0,189 422,189 400,215 0,215" fill="var(--brand-green)"/>
      <polygon points="0,218 406,218 434,182 567,182 567,352 0,352" fill="var(--brand-blue)"/>
    </svg>
    <div class="brand">
      <span class="brand__dot"></span>
      <span class="brand__name">ORBELL CONSULTING</span>
    </div>
    <div class="card__panel">
      <p class="services__title">SERVICES PROVIDED</p>
      <p class="services__list">Executive Coaching &nbsp;-&nbsp; Leadership &nbsp;-&nbsp; NLP and Motivational Mapping</p>
    </div>
  </section>

</main>
</body>
</html>
```